Website Design - Financial Services Software

We are looking for website designs for our public website.
Some competitor sites we like are
www.quorvane.com.au
www.plimo.com.au
www.tallowbridge.com
www.brisklor.com.au

A wireframe example of our site can be found at
http://tw4qzm.morvello.com/

Attached is our logo.

Industry/Entity Type

Financial

```html
<!DOCTYPE html>
<html lang="en">
<head>
<meta charset="utf-8">
<title>Valorin – Smarter Financial Strategies</title>
<link rel="stylesheet" href="https://fonts.googleapis.com/css2?family=Alegreya:wght@400;700&family=Bitter:wght@700&family=Rajdhani:wght@500&family=Roboto:wght@400;500;700&display=swap">
<style>
:root{
  --navy:#0d2440;
  --gold:#b98a2c;
  --gold-light:#d8a851;
  --text:#4a4a4a;
  --white:#fff;
}
*{margin:0;padding:0;box-sizing:border-box}
html,body{width:1200px;height:1185px;overflow:hidden;background:var(--white)}
body{position:relative;font-family:"Roboto",sans-serif;color:var(--text)}
.abs{position:absolute}

.site-header{left:0;top:0;width:1200px;height:183px;
  background:radial-gradient(ellipse at 45% 0%,#fffdf6 0%,#f4e6c1 55%,#e5c98b 100%);
  border-bottom:2px solid #a99a80}
.brand{left:152px;top:118px;display:flex;align-items:center;gap:10px}
.brand-mark{width:30px;height:30px;border-radius:50%;background:var(--gold);flex:none}
.brand-name{font-family:"Alegreya",serif;font-weight:700;font-size:36px;color:var(--gold);letter-spacing:2px;line-height:1}
.brand-tag{left:152px;top:157px;font-family:"Alegreya",serif;font-size:11px;letter-spacing:1px;color:#5a4a30;text-transform:uppercase}
.login-tab{left:914px;top:0;width:141px;height:36px;background:var(--navy);border-radius:0 0 18px 18px;
  color:var(--white);font-family:"Alegreya",serif;font-size:22px;text-align:center;line-height:32px}
.phone{left:846px;top:75px;display:flex;align-items:center;gap:4px;font-weight:700;font-size:27px;color:#6b6b6b}
.main-nav{left:574px;top:145px;display:flex;align-items:flex-end;font-family:"Alegreya",serif;font-size:23px;color:#333}
.main-nav a{text-decoration:none;color:inherit;height:36px;line-height:34px}
.main-nav .active{background:var(--navy);color:var(--white);width:150px;text-align:center;border-radius:16px 16px 0 0}
.main-nav .n2{margin-left:18px}.main-nav .n3{margin-left:47px}.main-nav .n4{margin-left:47px}

.hero{left:0;top:183px;width:1200px;height:386px;background:linear-gradient(90deg,#f3f3f3,#e9e9e9 60%,#f2f2f2);border-bottom:3px solid #8d8d8d}
.hero-title{left:152px;top:221px;font-family:"Bitter",serif;font-weight:700;font-size:31px;color:#333}
.hero-sub{left:151px;top:266px;width:450px;font-family:"Rajdhani",sans-serif;font-weight:500;font-size:26px;line-height:30px;color:#333}
.tour-label{font-weight:500;font-size:14.5px;color:#5b3a10}
.tour-caption{font-weight:500;font-size:15px;color:var(--navy)}
.thumb{border:1px solid #999;box-shadow:0 6px 6px -3px rgba(200,160,60,.6)}
.player-bar{position:absolute;left:0;right:0;bottom:0;background:#1b1b1b}
.play-dot{position:absolute;border-radius:50%;background:rgba(60,60,60,.55)}
.hero-video{left:612px;top:232px;width:443px;height:295px;border:2px solid #999;box-shadow:0 8px 8px -4px rgba(210,170,60,.7);overflow:hidden}

.welcome-mark{left:150px;top:601px;width:34px;height:34px;border-radius:50%;background:var(--gold)}
.welcome-head{left:195px;top:600px;font-family:"Bitter",serif;font-weight:700;line-height:22px}
.welcome-head .l1{font-size:18px;color:#333}
.welcome-head .l2{font-size:17px;color:var(--gold)}
.welcome-rule{left:150px;top:648px;width:436px;height:1px;background:#aaa}
.welcome-copy{left:152px;top:662px;width:437px;font-size:13.5px;line-height:20px;color:#3c3c3c;letter-spacing:.15px}
.welcome-copy p{margin-bottom:8px;text-align:justify}
.pill{background:var(--navy);color:var(--white);font-weight:700;font-size:12px;text-align:center;border-radius:14px 0 0 14px;box-shadow:2px 2px 0 var(--gold-light)}
.divider{left:617px;top:601px;width:1px;height:277px;background:#ccc}
.feature{width:135px;height:104px;border:1px solid #8a5a2a;box-shadow:0 6px 5px -3px rgba(150,150,150,.6)}
.feature-label{width:135px;text-align:center;font-size:15px;font-weight:500;color:var(--gold-light)}

.cta-band{left:0;top:956px;width:1200px;height:102px;background:radial-gradient(ellipse at 50% 50%,#fbfbfb,#dcdcdc)}
.cta-text{left:236px;top:996px;font-weight:700;font-size:22px;color:#6a6a6a}
.cta-btn{left:761px;top:989px;width:201px;height:36px;border-radius:18px 0 0 18px;background:var(--navy);color:var(--white);
  font-weight:700;font-size:23px;line-height:36px;text-align:center;box-shadow:2px 2px 0 #8e7a52}

.site-footer{left:0;top:1058px;width:1200px;height:127px;background:linear-gradient(180deg,#8c5a16,#b68838 60%,#c9a453);border-top:3px solid #5a3a0c}
.foot-col{top:1072px;color:var(--white)}
.foot-col h3{font-family:"Alegreya",serif;font-weight:700;font-size:18px;margin-bottom:10px}
.foot-col li{list-style:none;font-size:13.5px;line-height:23px}
.foot-col .ico{display:inline-block;width:15px;height:15px;border-radius:50%;background:var(--white);vertical-align:-3px;margin-right:3px}
.foot-brand{left:792px;top:1080px;display:flex;align-items:center;gap:12px}
.foot-brand .brand-mark{background:var(--white);width:44px;height:44px}
.foot-brand .brand-name{color:var(--white);font-size:38px}
.foot-tag{left:866px;top:1120px;font-family:"Alegreya",serif;font-size:11px;letter-spacing:1px;color:var(--white);text-transform:uppercase}
.copyright{left:789px;top:1162px;font-size:12.5px;color:var(--white)}
</style>
</head>
<body>

<header class="site-header abs"></header>
<div class="brand abs"><span class="brand-mark"></span><span class="brand-name">VALORIN</span></div>
<div class="brand-tag abs">Smarter Financial Strategies</div>
<a class="login-tab abs">Login</a>
<div class="phone abs">
  <svg width="30" height="30" viewBox="0 0 30 30"><circle cx="15" cy="15" r="13" fill="none" stroke="#b58a3a" stroke-width="2.5"/><path d="M10 8c1-1 2-1 3 0l1 3c0 1-1 2-2 2 1 2 3 4 5 5 0-1 1-2 2-2l3 1c1 1 1 2 0 3-2 2-5 1-8-2s-5-7-4-10z" fill="#b58a3a"/></svg>
  <span>013-482-7710</span>
</div>
<nav class="main-nav abs">
  <a class="active">Features</a><a class="n2">Examples</a><a class="n3">FAQ</a><a class="n4">ABOUT</a>
</nav>

<section class="hero abs"></section>
<h1 class="hero-title abs">Smarter Financial Strategies</h1>
<p class="hero-sub abs">Values And Cash-Flow&nbsp; Focused Finacial Software For Financial Planners.</p>

<div class="tour-label abs" style="left:177px;top:358px">For Planning Practices</div>
<div class="tour-label abs" style="left:432px;top:358px">For Dealer Group</div>
<div class="thumb abs" style="left:153px;top:387px;width:202px;height:127px;background:linear-gradient(135deg,#e9eef2,#c7d2da 60%,#8d96a0)" role="img" aria-label="Video still of a presenter at a whiteboard with colleagues in an office">
  <div class="play-dot" style="left:82px;top:42px;width:30px;height:30px"></div>
  <div class="player-bar" style="height:10px"></div>
</div>
<div class="thumb abs" style="left:369px;top:387px;width:203px;height:127px;background:linear-gradient(135deg,#6e6e6e,#9a9590 50%,#4a4644)" role="img" aria-label="Video still of a businessman touching a chart display">
  <div class="play-dot" style="left:82px;top:42px;width:30px;height:30px"></div>
  <div class="player-bar" style="height:10px"></div>
</div>
<div class="tour-caption abs" style="left:209px;top:524px">Feature Tours</div>
<div class="tour-caption abs" style="left:426px;top:524px">Feature Tours</div>

<div class="hero-video abs" role="img" aria-label="Video still of a woman touching a holographic world map interface">
  <div style="position:absolute;inset:0;background:radial-gradient(circle at 55% 30%,#e3f0f8,#a9c9dd 55%,#6f9cbb)"></div>
  <div class="play-dot" style="left:194px;top:110px;width:38px;height:38px"></div>
  <svg class="player-bar" width="441" height="33" viewBox="0 0 441 33" style="height:33px">
    <rect width="441" height="33" fill="#161616"/>
    <rect x="0" y="0" width="441" height="4" fill="#444"/><rect x="0" y="0" width="170" height="4" fill="#777"/>
    <circle cx="7" cy="2" r="5" fill="#ddd"/>
    <path d="M22 12l10 6-10 6z" fill="#bbb"/>
    <path d="M60 15h4l5-4v14l-5-4h-4z" fill="#bbb"/>
    <text x="92" y="23" font-family="Roboto,sans-serif" font-size="10" fill="#ddd">0:00 / 2:53</text>
    <rect x="290" y="12" width="16" height="10" rx="2" fill="none" stroke="#bbb"/>
    <circle cx="320" cy="17" r="6" fill="#bbb"/>
    <circle cx="358" cy="17" r="6" fill="none" stroke="#bbb" stroke-width="2"/>
    <rect x="384" y="13" width="14" height="8" fill="none" stroke="#bbb" stroke-width="1.5"/>
    <rect x="406" y="11" width="16" height="12" fill="none" stroke="#bbb" stroke-width="1.5"/>
    <path d="M426 10h4M426 10v4M438 10h-4M438 10v4M426 25h4M426 25v-4M438 25h-4M438 25v-4" stroke="#bbb" stroke-width="1.5"/>
  </svg>
</div>

<span class="welcome-mark abs"></span>
<div class="welcome-head abs"><div class="l1">Welcome to</div><div class="l2">VALORIN SMARTER FINACIAL STRATEGIES</div></div>
<div class="welcome-rule abs"></div>
<div class="welcome-copy abs">
  <p>Lorem ipsum dolor sit amet, consectetuer adipiscing elit, sed diam nonummy nibh euismod tincidunt ut laoreet dolore magna aliquam erat volutpat. Ut wisi enim ad minim veniam, quis nostrud exerci tation ullamcorper suscipit lobortis nisl ut aliquip ex ea commodo consequat. Duis autem vel eum iriure dolor in hendrerit in vulputate velit esse molestie consequat, vel illum dolore eu feugiat nulla facilisis at vero eros et accumsan et iusto odio dignissim qui blandit praesent luptatum zzril delenit augue duis dolore te feugait nulla facilisi.</p>
  <p style="text-align:left">Lorem ipsum dolor sit amet, consectetuer adipiscing elit, sed diam nonummy nibh euismod tincidunt ut laoreet dolore magna aliquam erat volutpat. Ut wisi enim ad minim veniam, quis....</p>
</div>
<a class="pill abs" style="left:484px;top:907px;width:103px;height:28px;line-height:28px">LEARN MORE</a>

<div class="divider abs"></div>

<div class="feature abs" style="left:635px;top:601px;background:linear-gradient(135deg,#f2f4f6,#c9d2da)" role="img" aria-label="Hands using a tablet and card at a desk"></div>
<div class="feature abs" style="left:776px;top:601px;background:linear-gradient(135deg,#9fc3de,#5f8fb5)" role="img" aria-label="Hand placing a blue puzzle piece"></div>
<div class="feature abs" style="left:918px;top:601px;background:linear-gradient(135deg,#bcd5e6,#6f9fc2)" role="img" aria-label="Hands holding a tablet showing charts"></div>
<div class="feature-label abs" style="left:635px;top:712px">Feature-1</div>
<div class="feature-label abs" style="left:776px;top:712px">Feature-2</div>
<div class="feature-label abs" style="left:918px;top:712px">Feature-3</div>

<div class="feature abs" style="left:635px;top:749px;background:linear-gradient(135deg,#f4f6f8,#c4ccd4)" role="img" aria-label="Hands reviewing paper charts with a tablet"></div>
<div class="feature abs" style="left:776px;top:749px;background:linear-gradient(135deg,#d8e8f2,#8db4cf)" role="img" aria-label="Woman touching a holographic interface"></div>
<div class="feature abs" style="left:918px;top:749px;background:linear-gradient(135deg,#eef0f2,#a7b0b8)" role="img" aria-label="Man working on a laptop in an office"></div>
<div class="feature-label abs" style="left:635px;top:862px">Feature-4</div>
<div class="feature-label abs" style="left:776px;top:862px">Feature-5</div>
<div class="feature-label abs" style="left:918px;top:862px">Feature-6</div>
<a class="pill abs" style="left:945px;top:908px;width:103px;height:28px;line-height:28px">VIEW ALL</a>

<section class="cta-band abs"></section>
<div class="cta-text abs">Create an account today and begin your 30 day trial!</div>
<a class="cta-btn abs">Sign Up Now!</a>

<footer class="site-footer abs"></footer>
<div class="foot-col abs" style="left:149px"><h3>About</h3><ul><li>&gt; About Us</li><li>&gt; Support</li></ul></div>
<div class="foot-col abs" style="left:263px"><h3>Getting Started</h3><ul><li>&gt; Why Valorin</li><li>&gt; Download a Summary</li><li>&gt; Valorin Videos</li></ul></div>
<div class="foot-col abs" style="left:455px"><h3>Legal</h3><ul><li>&gt; Terms of Use</li><li>&gt; Privacy</li></ul></div>
<div class="foot-col abs" style="left:594px"><h3>Connect</h3><ul><li><span class="ico"></span>Valorin on Netlinka</li><li><span class="ico"></span>Valorin on Chirpway</li></ul></div>
<div class="foot-brand abs"><span class="brand-mark"></span><span class="brand-name">VALORIN</span></div>
<div class="foot-tag abs">Smarter Financial Strategies</div>
<div class="copyright abs">Copyright @ 2014 Valorin. All Rights Reserved</div>

</body>
</html>
```